It's a new electrical company based in Newcastle NSW. I would like a logo between the two words "BRANO (insert logo) VOLT". I would like the logo to represent electrical and celtic style. For example I have seen a light bulb with a celtic pattern in the middle which looked very good. I would like it to be a white card, mainly black writing and quite basic not too much going on. But maybe have the logo partially red or green?

Reason: Waiting for new e mail address so I can put it on the business card

Industry/Entity Type

Electrical

Contact Information for Business Card

BRANO VOLT
Electrical Contractors
Domestic, commercial, fault finding, testing, re wires, switchboard upgrades
License No: 730482K
Fully Insured
Phone: 0487310294

```html
<!DOCTYPE html>
<html lang="en">
<head>
<meta charset="utf-8">
<title>Brano Volt – Business Card</title>
<link rel="stylesheet" href="https://fonts.googleapis.com/css2?family=Anton&family=EB+Garamond:wght@400;700&display=swap">
<style>
  :root {
    --card-bg: #ffffff;
    --ink: #1c1a1a;
    --accent-red: #d8241c;
    --frame: #9a9a9a;
  }
  html, body {
    margin: 0;
    padding: 0;
    width: 1200px;
    height: 776px;
    overflow: hidden;
    background: var(--card-bg);
  }
  .business-card {
    display: block;
    width: 1200px;
    height: 776px;
  }
  .card-frame { fill: var(--card-bg); stroke: var(--frame); stroke-width: 2; }
  .services-line {
    font-family: "EB Garamond", serif;
    font-weight: 400;
    font-size: 60px;
    fill: var(--ink);
  }
  .brand-name {
    font-family: "Anton", sans-serif;
    font-size: 236px;
    fill: var(--ink);
  }
  .brand-dot { fill: none; stroke: var(--accent-red); stroke-width: 16; }
  .brand-rule { fill: var(--ink); }
  .detail-line {
    font-family: "EB Garamond", serif;
    font-weight: 700;
    font-size: 68px;
    fill: var(--ink);
  }
</style>
</head>
<body>
<svg class="business-card" viewBox="0 0 1200 776" xmlns="http://www.w3.org/2000/svg" role="img" aria-label="Brano Volt electrical contractors business card">
  <rect class="card-frame" x="1" y="1" width="1198" height="774"/>

  <text class="services-line" x="72" y="98" textLength="1060" lengthAdjust="spacingAndGlyphs">Electrical Contractors Domestic, commercial</text>

  <g class="brand-lockup">
    <text class="brand-name" x="110" y="360" textLength="370" lengthAdjust="spacingAndGlyphs">Brano</text>
    <circle class="brand-dot" cx="600" cy="274" r="78"/>
    <text class="brand-name" x="730" y="360" textLength="360" lengthAdjust="spacingAndGlyphs">Volt</text>
  </g>
  <rect class="brand-rule" x="110" y="414" width="980" height="7"/>

  <text class="detail-line" x="110" y="560" textLength="980" lengthAdjust="spacingAndGlyphs">Switchboard License No: 730482K</text>
  <text class="detail-line" x="110" y="648" textLength="980" lengthAdjust="spacingAndGlyphs">Fully Insured Phone: 0487310294</text>
</svg>
</body>
</html>
```